Rebrand of 3 bottle labels for nail polish brand

The task is to make a rebranding of our current gel nail polish bottle design. We have become one of the leading european nail polish brand, so we want to improve the quality of the label design to a more scandinavian and minimalistic bottle design, which stille has to be recognisable and unique.

We have attached a more detailed description of the rebranding instructions for our gel polish bottles called "bottle task".
Updates

The Labels should not be just Black and White as stated. But should be mainly Black and White and then some of our color as explained in the uploaded file.

Target Market(s)

Girls and women age 18-55 Northern Europe

Industry/Entity Type

Cosmetic/ Nail Gel Polish

Colors

Designer to choose only greyscale colors for use in the design.

Requirements
Must have
• See attched design instruction
Nice to have
• Moderne, Minimalist, Recognizable and Unique look
Should not have
• Too many elements, too busy design

```html
<!DOCTYPE html>
<html lang="en">
<head>
<meta charset="utf-8">
<title>lakkora – gel polish labels</title>
<link rel="stylesheet" href="https://fonts.googleapis.com/css2?family=Quicksand:wght@500&family=Roboto:wght@500;700&display=swap">
<style>
  :root {
    --bg: #ffffff;
    --label: #0b0b0b;
    --ink: #ffffff;
    --nude: #c9a296;
    --nude-text: #3a2a25;
    --red: #b3171d;
    --fine: #b89a8f;
  }
  * { margin: 0; padding: 0; box-sizing: border-box; }
  html, body { width: 1200px; height: 1000px; overflow: hidden; background: var(--bg); }
  .canvas { position: relative; width: 1200px; height: 1000px; background: var(--bg); }

  .label {
    position: absolute;
    background: var(--label);
    color: var(--ink);
    border-radius: 18px;
    display: flex;
    flex-direction: column;
    align-items: center;
    font-family: 'Quicksand', sans-serif;
  }
  .label--base    { left: 70px;  top: 560px; width: 310px; height: 310px; }
  .label--color   { left: 455px; top: 560px; width: 310px; height: 310px; }
  .label--remover { left: 835px; top: 330px; width: 290px; height: 560px; border-radius: 40px; }

  .brand {
    font-family: 'Roboto', sans-serif;
    font-weight: 500;
    font-size: 46px;
    line-height: 1;
    letter-spacing: 4px;
    margin-top: 44px;
  }
  .label--remover .brand { font-size: 50px; margin-top: 110px; }

  .product {
    font-size: 23px;
    font-weight: 500;
    letter-spacing: 0.5px;
    line-height: 1;
    margin-top: 16px;
  }
  .method {
    font-size: 14px;
    font-weight: 500;
    letter-spacing: 0.5px;
    margin-top: 3px;
  }

  .shade { position: relative; width: 100%; height: 56px; margin-top: 10px; }
  .shade__number {
    position: absolute; left: 50%; top: 0; transform: translateX(-50%);
    width: 42px; height: 30px; border-radius: 4px 4px 0 0;
    font-family: 'Roboto', sans-serif; font-weight: 500; font-size: 20px;
    display: flex; align-items: center; justify-content: center;
  }
  .shade__name {
    position: absolute; left: 50%; top: 28px; transform: translateX(-50%);
    width: 180px; height: 27px; border-radius: 4px 4px 14px 14px;
    font-family: 'Roboto', sans-serif; font-weight: 700; font-size: 15px;
    display: flex; align-items: center; justify-content: center; letter-spacing: 0.3px;
  }
  .shade--nude .shade__number { border: 2px solid var(--nude); color: var(--ink); }
  .shade--nude .shade__name { background: var(--nude); color: var(--nude-text); }
  .shade--red .shade__number { background: var(--red); color: var(--ink); }
  .shade--red .shade__name { background: var(--red); color: var(--ink); }
  .shade__band { position: absolute; top: 28px; height: 27px; width: 50px; background: var(--red); }
  .shade__band--left  { left: 0;  border-radius: 0 14px 14px 0; }
  .shade__band--right { right: 0; border-radius: 14px 0 0 14px; }

  .claim {
    font-family: 'Roboto', sans-serif; font-weight: 700; font-size: 17px;
    margin-top: 6px; letter-spacing: 0.3px;
  }

  .remover-name {
    font-size: 29px; font-weight: 500; letter-spacing: 1.5px;
    text-align: center; line-height: 1.4; margin-top: 26px;
  }
  .remover-shade {
    width: 60px; height: 40px; margin-top: 44px;
    background: var(--nude); color: var(--nude-text); border-radius: 4px;
    font-family: 'Roboto', sans-serif; font-weight: 500; font-size: 24px;
    display: flex; align-items: center; justify-content: center;
  }
  .volume {
    font-family: 'Roboto', sans-serif; font-weight: 500; font-size: 12px;
    color: var(--fine); margin-top: auto; margin-bottom: 60px; letter-spacing: 0.3px;
  }
</style>
</head>
<body>
<div class="canvas">

  <section class="label label--base">
    <div class="brand">LAKKORA</div>
    <div class="product">BASE COAT</div>
    <div class="method">SOAK OFF UV/LED</div>
    <div class="shade shade--nude">
      <div class="shade__number">01</div>
      <div class="shade__name">SUPPLE</div>
    </div>
    <div class="claim">Vegan Formula</div>
  </section>

  <section class="label label--color">
    <div class="brand">LAKKORA</div>
    <div class="product">COLOR COAT</div>
    <div class="method">SOAK OFF UV/LED</div>
    <div class="shade shade--red">
      <div class="shade__band shade__band--left"></div>
      <div class="shade__number">21</div>
      <div class="shade__name">DEEP CHERRY</div>
      <div class="shade__band shade__band--right"></div>
    </div>
    <div class="claim">Vegan Formula</div>
  </section>

  <section class="label label--remover">
    <div class="brand">LAKKORA</div>
    <div class="remover-name">GEL POLISH<br>REMOVER</div>
    <div class="remover-shade">21</div>
    <div class="volume">120ml e 4fl.oz</div>
  </section>

</div>
</body>
</html>
```